Design us a professional website for a Cannabis Staffing Agency

We already have a logo ready to go, but now we are looking for a few good web designs. We provide staffing for the Cannabis/Marijuana industry. We want a good balance of clean, simple and modern design but also embracing the exciting atmosphere of the Cannabis industry.

Here are examples of our competition, please note that most of these competitors design feel old and dated:

http://qrvplacementcrew.example/
https://tolbrix.example/tolbrix-main-page
http://saffronpathways.example/index.html
http://www.wickcrew.example/medical-marijuana-staffing-recruiting
http://www.tundrahiring.example/
www.placedupcrew.example
www.pinewise.example

I also would prefer an explanation of why you choose to design it the way you did? What was your thought process or did you use a template?

Requirements
Must have
• About Us Page
• Candidates Page
• Employer Page
• Job Opening Page
• Contact Us Page
Nice to have
• Colors to match the logo, good use of images and design to show the story. Our goal is to show our clients what we are about and not just tell them.

```html
<!DOCTYPE html>
<html lang="en">
<head>
<meta charset="utf-8">
<title>LEAFWORK – Cannabis Staffing Agency</title>
<link rel="stylesheet" href="https://fonts.googleapis.com/css2?family=Montserrat:wght@400;500;600;700;800&family=Playfair+Display:ital@1&display=swap">
<style>
:root{
  --green:#5e9b0c;
  --green-dark:#3f6a07;
  --green-deep:#2f4f08;
  --ink:#333333;
  --muted:#6b6b6b;
  --light:#f3f3f3;
  --grey:#ececec;
  --dark:#3a3a3a;
  --darker:#2a2a2a;
  --field:#1f1f1f;
  --gold:#e0a526;
  --white:#ffffff;
}
*{box-sizing:border-box;margin:0;padding:0}
html,body{width:1200px;height:3053px;overflow:hidden}
body{position:relative;font-family:"Montserrat",Arial,sans-serif;color:var(--ink);background:var(--white)}
ul{list-style:none}

/* header */
.site-header{position:absolute;left:0;top:0;width:1200px;height:82px;background:var(--white)}
.brand{position:absolute;left:231px;top:14px;display:flex;align-items:center;gap:10px}
.brand-dot{width:50px;height:50px;border-radius:50%;background:var(--green)}
.brand-name{font-weight:700;font-size:30px;color:var(--green);letter-spacing:1px}
.top-icons{position:absolute;top:14px;left:812px;display:flex;gap:6px}
.top-icons span{width:24px;height:24px;border-radius:50%;border:1.5px solid var(--green);display:flex;align-items:center;justify-content:center}
.top-icons .gap{margin-left:14px;border-color:#777}
.main-nav{position:absolute;top:46px;left:558px;display:flex;gap:22px;font-size:10.5px;font-weight:600;color:#444}
.main-nav .active{color:var(--green)}

/* hero */
.hero{position:absolute;left:0;top:82px;width:1200px;height:429px;background:linear-gradient(180deg,#5f9c0d,#5a950a)}
.hero-photo{position:absolute;inset:0;background:repeating-linear-gradient(90deg,rgba(255,255,255,.04) 0 60px,rgba(0,0,0,.04) 60px 120px)}
.hero-title{position:absolute;top:72px;width:100%;text-align:center;font-size:45px;font-weight:700;color:#34450f}
.hero-rule{position:absolute;top:124px;left:288px;width:624px;height:2px;background:#34450f;opacity:.6}
.hero-sub{position:absolute;top:130px;width:100%;text-align:center;font-size:31px;font-weight:700;color:var(--white);line-height:34px}
.cta{position:absolute;top:245px;width:360px;height:107px;border:3px solid rgba(255,255,255,.75);background:rgba(47,79,8,.55);text-align:center;color:var(--white)}
.cta h2{font-size:33px;font-weight:600;margin-top:12px}
.cta p{font-size:10px;font-weight:600;margin-top:4px}
.cta a{position:absolute;left:50%;transform:translateX(-50%);bottom:-18px;width:152px;height:37px;line-height:37px;background:var(--white);color:#333;font-size:11px;font-weight:600;text-decoration:none}

/* about */
.about{position:absolute;left:0;top:511px;width:1200px;height:395px;background:var(--light)}
.about-photo{position:absolute;right:0;top:10px;width:330px;height:385px;background:linear-gradient(90deg,rgba(243,243,243,1),#d9dde0 30%,#b9c2c8)}
.about h2{position:absolute;left:231px;top:95px;font-size:40px;font-weight:800;color:var(--green)}
.about h3{position:absolute;left:231px;top:137px;font-size:19px;font-weight:700;color:var(--ink)}
.rule{height:3px;width:100px;background:var(--green)}
.about .rule{position:absolute;left:231px;top:168px}
.about p{position:absolute;left:231px;top:187px;width:430px;font-size:12.5px;line-height:19.5px;color:var(--muted)}
.stats{position:absolute;left:726px;top:100px;width:232px;height:178px;display:grid;grid-template-columns:1fr 1fr}
.stat{text-align:center;padding-top:10px}
.stat:nth-child(1),.stat:nth-child(3){border-right:1px solid #ccc}
.stat:nth-child(1),.stat:nth-child(2){border-bottom:1px solid #ccc}
.stat b{display:block;font-size:34px;font-weight:700;color:#444}
.stat span{display:block;font-size:9px;color:#555;line-height:13px;margin-top:4px}

/* offering */
.offering{position:absolute;left:0;top:906px;width:1200px;height:354px;background:var(--grey)}
.off-photo{position:absolute}
.col-title{position:absolute;font-size:20px;font-weight:700;color:var(--green)}
.col-list{position:absolute;font-size:12.5px;line-height:18.8px;color:#444}
.offering h2{position:absolute;right:235px;top:90px;font-size:40px;font-weight:800;color:var(--green)}
.offering p{position:absolute;right:235px;top:145px;width:305px;text-align:right;font-size:12px;line-height:19px;color:#555}

/* career advice */
.advice{position:absolute;left:0;top:1260px;width:1200px;height:515px;background:var(--white)}
.section-title{position:absolute;left:0;width:100%;text-align:center;font-size:34px;font-weight:700;color:var(--ink)}
.card{position:absolute;top:147px;width:215px}
.card-img{height:163px;border-radius:40px 0 40px 0}
.card h4{margin-top:20px;font-size:13.5px;line-height:15px;font-weight:700;color:var(--green)}
.card p{margin-top:8px;font-size:10px;line-height:13px;color:#666}
.card a{display:block;margin-top:18px;width:102px;height:33px;line-height:33px;text-align:center;background:var(--dark);color:var(--white);font-size:10px;font-weight:700;text-decoration:none}

/* testimonials & contact */
.reviews{position:absolute;left:0;top:1775px;width:1200px;height:961px;background:#efefef}
.reviews .lead{position:absolute;top:125px;width:100%;text-align:center;font-size:12px;color:#555}
.stars{position:absolute;top:168px;width:100%;text-align:center;color:var(--gold);font-size:13px;letter-spacing:4px}
.quote{position:absolute;left:380px;top:203px;width:440px;text-align:center;font-family:"Playfair Display",Georgia,serif;font-style:italic;font-size:16.5px;line-height:19.5px;color:#555}
.avatar{position:absolute;border-radius:50%;background:#d6cbc3}
.avatar.faded{opacity:.5}
.avatar.main{border:3px solid var(--green);background:#b9978a}
.reviewer{position:absolute;top:416px;width:100%;text-align:center;font-size:11px;font-weight:700;color:#444}
.role{position:absolute;top:432px;width:100%;text-align:center;font-size:8px;color:#999}
.dark-band{position:absolute;left:0;top:0}
.contact-title{position:absolute;left:231px;top:660px;font-size:29px;font-weight:700;color:var(--white)}
.contact-rule{position:absolute;left:231px;top:705px}
.contact-info{position:absolute;left:231px;top:735px;font-size:12px;line-height:17px;color:#ddd}
.circle-icons{position:absolute;display:flex;gap:6px}
.circle-icons span{width:34px;height:34px;border-radius:50%;border:1.5px solid var(--green)}
.field{position:absolute;left:652px;width:313px;background:var(--field);color:#bbb;font-size:11px;padding:11px 12px}
.captcha{position:absolute;top:898px;left:652px;width:100px;height:31px;background:var(--white);font-size:17px;letter-spacing:3px;color:#222;line-height:31px;text-align:center;font-family:"Courier New",monospace}
.captcha-input{position:absolute;top:898px;left:756px;width:98px;height:31px;background:var(--field);color:#bbb;font-size:10px;line-height:31px;padding-left:10px}
.submit{position:absolute;top:898px;left:861px;width:104px;height:31px;background:var(--green);color:var(--white);font-size:11px;font-weight:700;line-height:31px;text-align:center}

/* footer */
.site-footer{position:absolute;left:0;top:2736px;width:1200px;height:317px;background:var(--darker);color:#bbb}
.site-footer .brand{left:231px;top:64px;gap:8px}
.site-footer .brand-dot{width:46px;height:46px}
.site-footer .brand-name{font-size:23px;letter-spacing:.5px}
.legal{position:absolute;left:288px;top:132px;font-size:10px;line-height:15px}
.legal b{color:#eee;font-weight:600}
.foot-title{position:absolute;top:76px;font-size:14px;font-weight:700;color:var(--green)}
.foot-text{position:absolute;left:464px;top:106px;width:225px;font-size:9.5px;line-height:13.5px}
.foot-links{position:absolute;left:724px;top:104px;font-size:9.5px;line-height:15.5px}
.copyright{position:absolute;top:270px;width:100%;text-align:center;font-size:10px;color:#ddd}
</style>
</head>
<body>

<header class="site-header">
  <div class="brand"><span class="brand-dot"></span><span class="brand-name">LEAFWORK</span></div>
  <div class="top-icons">
    <span></span><span></span><span></span>
    <span class="gap"><svg width="12" height="12" viewBox="0 0 24 24"><path d="M6.6 10.8a15 15 0 006.6 6.6l2.2-2.2c.3-.3.7-.4 1-.2 1.1.4 2.3.6 3.6.6.6 0 1 .4 1 1V20c0 .6-.4 1-1 1A17 17 0 013 4c0-.6.4-1 1-1h3.5c.6 0 1 .4 1 1 0 1.3.2 2.5.6 3.6.1.3 0 .7-.2 1z" fill="#555"/></svg></span>
    <span style="border-color:#777"><svg width="12" height="12" viewBox="0 0 24 24"><rect x="2" y="5" width="20" height="14" rx="2" fill="none" stroke="#555" stroke-width="2"/><path d="M2 6l10 7 10-7" fill="none" stroke="#555" stroke-width="2"/></svg></span>
  </div>
  <nav class="main-nav"><span class="active">HOME</span><span>ABOUT US</span><span>JOB SEEKERS</span><span>EMPLOYERS</span><span>RESOURCES</span><span>CONTACT</span></nav>
</header>

<section class="hero">
  <div class="hero-photo" role="img" aria-label="Grid of smiling job candidate portraits tinted green"></div>
  <h1 class="hero-title">Connecting People with Jobs</h1>
  <div class="hero-rule"></div>
  <p class="hero-sub">We Work Hard For You To Meet Your<br>Staffing Needs</p>
  <div class="cta" style="left:231px"><h2>Job Seekers</h2><p>LOOKING FOR EMPLOYMENT? CLIMB YOUR WAY TO THE TOP!</p><a href="#">FIND YOUR CAREER</a></div>
  <div class="cta" style="left:607px"><h2>Employers</h2><p>ACHIEVE YOUR STAFFING GOALS. FIND YOUR CANDIDATE RIGHT HERE</p><a href="#">FIND GREAT TALENT</a></div>
</section>

<section class="about">
  <div class="about-photo" role="img" aria-label="Two colleagues reviewing work together at a desk"></div>
  <h2>LEAFWORK</h2>
  <h3>Largest and leading cannabis staffing agency.</h3>
  <div class="rule"></div>
  <p>Sed ut perspiciatis unde omnis iste natus error sit voluptatem accusantium doloremque laudantium, totam rem aperiam, eaque ipsa quae ab illo inventore veritatis et quasi architecto beatae vitae dicta sunt explicabo. Nemo enim ipsam voluptatem quia voluptas sit aspernatur aut odit aut fugit, sed quia consequuntur magni dolores eos qui ratione voluptatem sequi nesciunt. Neque porro quisquam est.</p>
  <div class="stats">
    <div class="stat"><b>44</b><span>MEDICAL MARIJUANA<br>STATES</span></div>
    <div class="stat"><b>08</b><span>LEGAL MARIJUANA<br>STATES</span></div>
    <div class="stat"><b>05</b><span>HAPPY RECRUITERS</span></div>
    <div class="stat"><b>256</b><span>CUPS OF COFFEE</span></div>
  </div>
</section>

<section class="offering">
  <div class="off-photo" role="img" aria-label="Hand typing on a white keyboard beside a mouse" style="left:0;top:0;width:330px;height:180px;background:linear-gradient(135deg,#f7f7f7,#dcdcdc)"></div>
  <div class="off-photo" role="img" aria-label="Yellow wristwatch on the desk" style="right:0;top:40px;width:130px;height:120px;background:radial-gradient(circle at 60% 50%,#e8c640,#ececec 70%)"></div>
  <div class="off-photo" role="img" aria-label="Smartphone corner on the desk" style="right:0;top:295px;width:100px;height:59px;background:linear-gradient(160deg,#ececec,#c9c9c9)"></div>
  <h3 class="col-title" style="left:231px;top:96px">POSITIONS</h3>
  <ul class="col-list" style="left:231px;top:133px"><li>Patient Consultants</li><li>Patient Liaisons</li><li>Expo Presenters</li><li>Trimming</li><li>Cultivation</li><li>Management</li><li>Payroll</li></ul>
  <h3 class="col-title" style="left:409px;top:96px">PERKS</h3>
  <ul class="col-list" style="left:409px;top:133px"><li>In-House Training</li><li>Last Minute Positions</li><li>Fully Bonded</li><li>Worker's Comp</li><li>Cultivation</li><li>In-House Payroll</li><li>Excellent Customer Service 24/7</li></ul>
  <h2>OFFERING JOBS</h2>
  <p>At Saffron Pathways, we offer a range of options that cater directly &amp; personally to your business. We believe in working as a partner to our clients to improve their bottom line and cultivate comprehensive solutions to their staffing needs.</p>
</section>

<section class="advice">
  <h2 class="section-title" style="top:62px">CAREER ADVICE</h2>
  <article class="card" style="left:252px"><div class="card-img" role="img" aria-label="Busy cafe interior with warm lights" style="background:linear-gradient(135deg,#5a3b22,#c7803a)"></div><h4>NEMO ENIM VOLUPTATEM<br>QUIA VOLUPTAS</h4><p>Quis autem vel eum iure reprehenderit qui in ea voluptate velit esse quam nihil.</p><a href="#">READ MORE</a></article>
  <article class="card" style="left:499px"><div class="card-img" role="img" aria-label="Wooden desk with an orange chair and notebook" style="background:linear-gradient(135deg,#e2622c,#c9a27a 55%,#e8dccb)"></div><h4>NEMO ENIM VOLUPTATEM<br>QUIA VOLUPTAS</h4><p>Quis autem vel eum iure reprehenderit qui in ea voluptate velit esse quam nihil.</p><a href="#">READ MORE</a></article>
  <article class="card" style="left:740px"><div class="card-img" role="img" aria-label="Hands holding a tablet" style="background:linear-gradient(135deg,#d9dfe6,#9a7a66 60%,#2d2d33)"></div><h4>NEMO ENIM VOLUPTATEM<br>QUIA VOLUPTAS</h4><p>Quis autem vel eum iure reprehenderit qui in ea voluptate velit esse quam nihil.</p><a href="#">READ MORE</a></article>
</section>

<section class="reviews">
  <svg class="dark-band" width="1200" height="961" viewBox="0 0 1200 961" role="img" aria-label="Dark panel with faint leaf texture">
    <polygon points="0,454 600,577 1200,389 1200,961 0,961" fill="#3a3a3a"/>
  </svg>
  <h2 class="section-title" style="top:75px">WHAT CLIENTS SAY?</h2>
  <p class="lead">Read our favorite reviews about our Job Platform from our clients.</p>
  <div class="stars">★★★★★</div>
  <p class="quote">“Sed ut perspiciatis unde omnis iste natus error sit voluptatem accusantium doloremque laudantium, totam rem aperiam, eaque ipsa quae ab illo inventore veritatis et quasi architecto beatae vitae dicta sunt explicabo. Nemo enim ipsam voluptatem quia.”</p>
  <div class="avatar faded" style="left:381px;top:348px;width:40px;height:40px"></div>
  <div class="avatar faded" style="left:477px;top:348px;width:40px;height:40px"></div>
  <div class="avatar main" role="img" aria-label="Reviewer portrait" style="left:558px;top:333px;width:70px;height:70px"></div>
  <div class="avatar faded" style="left:669px;top:348px;width:40px;height:40px"></div>
  <div class="avatar faded" style="left:765px;top:348px;width:40px;height:40px"></div>
  <p class="reviewer">MARLOW PENN</p>
  <p class="role">WEB DESIGNER</p>

  <h2 class="contact-title">Get in touch with us today!</h2>
  <div class="rule contact-rule"></div>
  <div class="contact-info">
    <p>Level 9/45 Ferrow St Ashvale Vic 3999</p>
    <p style="margin-top:20px">Phone: 03 5550 0142</p>
    <p>Fax: 03 5550 0187</p>
    <p>Email: info@leafwork.example</p>
  </div>
  <div class="circle-icons" style="left:231px;top:837px"><span></span><span></span><span></span></div>
  <div class="field" style="top:658px;height:33px">Name*</div>
  <div class="field" style="top:703px;height:33px">Email*</div>
  <div class="field" style="top:748px;height:33px">Phone*</div>
  <div class="field" style="top:793px;height:99px">Enquiry:</div>
  <div class="captcha">W6 8HP</div>
  <div class="captcha-input">Enter Captcha</div>
  <div class="submit">SUBMIT</div>
</section>

<footer class="site-footer">
  <div class="brand"><span class="brand-dot"></span><span class="brand-name">LEAFWORK</span></div>
  <div class="legal"><b>LEAFWORK PTY LTD</b><br><br>Level 9/45 Ferrow St<br>Ashvale Vic 3999<br><br>03 5550 0142</div>
  <h4 class="foot-title" style="left:464px">ABOUT LEAFWORK</h4>
  <p class="foot-text">Sed ut perspiciatis unde omnis iste natus error sit voluptatem accusantium doloremque laudantium, totam rem aperiam, eaque ipsa quae ab illo inventore veritatis et quasi architecto beatae vitae dicta sunt explicabo. Nemo enim ipsam voluptatem quia voluptas sit aspernatur aut odit aut fugit, sed quia consequuntur magni.</p>
  <h4 class="foot-title" style="left:724px">QUICKLINKS</h4>
  <ul class="foot-links"><li>- HOME</li><li>- ABOUT US</li><li>- JOB SEEKERS</li><li>- EMPLOYERS</li><li>- RESOURCES</li><li>- CONTACT</li></ul>
  <h4 class="foot-title" style="left:857px">SOCIAL MEDIA</h4>
  <div class="circle-icons" style="left:855px;top:106px"><span></span><span></span><span></span></div>
  <p class="copyright">Copyright © 2017 LEAFWORK. All rights reserved. Terms &amp; Conditions &nbsp;|&nbsp; Privacy Policy</p>
</footer>

</body>
</html>
```